Redesign Colorful Business Card

Please redesign the card attached. It is too busy. Please don't eliminate any of the words. The repetivite word "free" can be used less often.

Target Market(s)

College Students.

Contact Information for Business Card

The details listed in the attached image

Font styles to use
Sans Serif

Requirements
Must have
• A clear and simple presentation and must be attractive.

```html
<!DOCTYPE html>
<html lang="en">
<head>
<meta charset="utf-8">
<title>StudyNimbl Card</title>
<link href="https://fonts.googleapis.com/css2?family=Poppins:wght@600;700&display=swap" rel="stylesheet">
<style>
  :root {
    --sky: #87cff5;
    --navy: #1c4a94;
    --ink: #222222;
    --white: #ffffff;
    --yellow: #f5df2e;
    --blue-soft: #4d86c8;
  }
  * { margin: 0; padding: 0; box-sizing: border-box; }
  html, body {
    width: 1200px;
    height: 686px;
    overflow: hidden;
    background: var(--white);
  }
  .card {
    position: relative;
    width: 1200px;
    height: 686px;
    background: var(--sky);
    border-radius: 24px;
    overflow: hidden;
    font-family: "Poppins", Arial, sans-serif;
    color: var(--ink);
  }
  .benefit {
    position: absolute;
    font-weight: 600;
    font-size: 34px;
    line-height: 44px;
  }
  .benefit--time { left: 126px; top: 88px; text-align: left; }
  .benefit--memory { right: 126px; top: 88px; text-align: right; }
  .benefit--class { left: 0; width: 1200px; top: 266px; text-align: center; }
  .timeline {
    position: absolute;
    left: 200px;
    top: 180px;
    width: 800px;
    height: 70px;
  }
  .brand {
    position: absolute;
    left: 69px;
    top: 534px;
    display: flex;
    align-items: center;
    gap: 14px;
  }
  .brand__mark {
    width: 80px;
    height: 80px;
    background: var(--navy);
    border-radius: 6px;
  }
  .brand__name {
    font-weight: 700;
    font-size: 43px;
    color: var(--ink);
    text-decoration: underline;
    text-decoration-thickness: 3px;
    text-underline-offset: 6px;
  }
  .promo-art {
    position: absolute;
    left: 872px;
    top: 388px;
    width: 226px;
    height: 246px;
    border-radius: 18px;
    background: linear-gradient(160deg, var(--navy) 0%, var(--blue-soft) 55%, var(--yellow) 100%);
  }
  .promo-label {
    position: absolute;
    left: 872px;
    top: 432px;
    width: 226px;
    text-align: center;
    font-weight: 600;
    font-size: 50px;
    line-height: 60px;
    letter-spacing: 5px;
    color: var(--white);
  }
</style>
</head>
<body>
  <main class="card">
    <p class="benefit benefit--time">Cut Study Time<br>Down By Up To 50%</p>
    <p class="benefit benefit--memory">Memorize Anything<br>Quickly</p>

    <svg class="timeline" viewBox="0 0 800 70" aria-hidden="true">
      <rect x="30" y="22" width="740" height="22" rx="11" fill="var(--white)"/>
      <rect x="30" y="27" width="740" height="12" fill="var(--navy)"/>
      <circle cx="37" cy="33" r="24" fill="var(--white)"/>
      <circle cx="37" cy="33" r="18" fill="var(--navy)"/>
      <circle cx="400" cy="33" r="24" fill="var(--white)"/>
      <circle cx="400" cy="33" r="18" fill="var(--navy)"/>
      <circle cx="763" cy="33" r="24" fill="var(--white)"/>
      <circle cx="763" cy="33" r="18" fill="var(--navy)"/>
    </svg>

    <p class="benefit benefit--class">Learn A Subject<br>Without Having To<br>Go To Class</p>

    <div class="brand">
      <span class="brand__mark"></span>
      <span class="brand__name">StudyNimbl.com</span>
    </div>

    <div class="promo-art" role="img" aria-label="Illustration of a yellow megaphone with a speech bubble announcing a free offer"></div>
    <p class="promo-label">FREE</p>
  </main>
</body>
</html>
```